New Infographic-y Sales Diagram

We've got an asset affectionately known as "The Pebble," that needs a major update. First, we need a new logo applied. Second, we need the entire former design scrapped in favor of something better. Literally nothing should remain the same.

If you approximate the files given as a reference that would be enough. If, however, you can achieve something even better that we hadn't considered--that would truly be wonderful.

Target Market(s)

Homeowners. Preferably ones looking to make updates to their home. We do functional home renovations for folks.

Industry/Entity Type

Home Improvement

Font styles to use
Sans Serif

Colors

Designer to choose colors to be used in the design.

Requirements
Must have
• Some illustration work and and a generally unified theme.
Should not have
• Clip art or stock assets (excluding photography and icons if the icons are excellent).

```html
<!DOCTYPE html>
<html lang="en">
<head>
<meta charset="utf-8">
<title>Brightmoss Energy – Control, Conserve, Create</title>
<link href="https://fonts.googleapis.com/css2?family=Questrial&display=swap" rel="stylesheet">
<style>
  :root {
    --bg: #ffffff;
    --ink: #111111;
    --cyan: #4ff0f5;
    --cyan-soft: #8af4f7;
    --green: #4de83a;
    --orange: #ff7a1a;
    --orange-soft: #ffa35c;
    --brand-orange: #f26a1f;
    --card: #ffffff;
    --shadow: rgba(0, 0, 0, 0.35);
  }
  * { margin: 0; padding: 0; box-sizing: border-box; }
  html, body { width: 849px; height: 1200px; overflow: hidden; background: var(--bg); }
  body { font-family: "Questrial", sans-serif; color: var(--ink); position: relative; }

  .brand {
    position: absolute; top: 50px; left: 0; width: 849px;
    display: flex; justify-content: center; align-items: center; gap: 10px;
  }
  .brand-dot { width: 30px; height: 30px; border-radius: 50%; background: var(--brand-orange); }
  .brand-name { font-size: 36px; color: var(--brand-orange); line-height: 1; }

  .home-scene {
    position: absolute; left: 82px; top: 156px; width: 686px; height: 300px;
    background: linear-gradient(180deg, #ffffff 0%, #dffcfd 100%);
    border-radius: 6px;
  }

  .card {
    position: absolute; background: var(--card);
    box-shadow: 0 0 10px var(--shadow);
    text-align: center;
  }
  .card--control { left: 14px; top: 556px; width: 254px; height: 546px; }
  .card--create { left: 568px; top: 556px; width: 262px; height: 546px; }
  .card--conserve { left: 268px; top: 518px; width: 299px; height: 622px; z-index: 2; }

  .card-title { position: absolute; left: 0; width: 100%; font-size: 39px; font-weight: 400; line-height: 1; }
  .card--control .card-title { top: 9px; color: var(--green); }
  .card--create .card-title { top: 9px; color: var(--orange); }
  .card--conserve .card-title { top: 21px; color: var(--cyan); }

  .card-lede {
    position: absolute; left: 12px; right: 12px; font-size: 13px; line-height: 16px;
    color: var(--cyan-soft);
  }
  .card--control .card-lede { top: 84px; }
  .card--conserve .card-lede { top: 120px; left: 42px; right: 42px; }
  .card--create .card-lede { top: 84px; color: var(--orange-soft); }

  .card-list { position: absolute; left: 0; width: 100%; list-style: none; }
  .card--control .card-list { top: 191px; font-size: 18.5px; line-height: 32px; }
  .card--conserve .card-list { top: 228px; font-size: 29px; line-height: 46px; }
  .card--create .card-list { top: 238px; font-size: 24px; line-height: 39px; }

  .choose-btn {
    position: absolute; width: 179px; height: 56px;
    border: 2px solid var(--cyan); border-radius: 28px;
    background: transparent; color: var(--cyan-soft);
    font-family: "Questrial", sans-serif; font-size: 26px;
    display: flex; align-items: center; justify-content: center;
  }
  .card--control .choose-btn { left: 44px; top: 478px; }
  .card--create .choose-btn { left: 42px; top: 478px; }
  .card--conserve .choose-btn { left: 66px; top: 556px; }
</style>
</head>
<body>
  <header class="brand">
    <span class="brand-dot"></span>
    <span class="brand-name">brightmoss energy</span>
  </header>

  <div class="home-scene" role="img" aria-label="Line illustration of a two-storey family house flanked by trees"></div>

  <section class="card card--control">
    <h2 class="card-title">Control</h2>
    <p class="card-lede">High Comfort, Low cost upgrades that change the way you use the energy</p>
    <ul class="card-list">
      <li>HAVC</li>
      <li>LED Lighting</li>
      <li>Smart Thermostat</li>
      <li>Smart Sensors</li>
    </ul>
    <button class="choose-btn">Choose</button>
  </section>

  <section class="card card--conserve">
    <h2 class="card-title">Conserve</h2>
    <p class="card-lede">Simple additions that cut out energy waste without cutting in to your life.</p>
    <ul class="card-list">
      <li>Patio Covers</li>
      <li>Water Heater</li>
      <li>Insulation</li>
      <li>Windows</li>
      <li>Roofing</li>
    </ul>
    <button class="choose-btn">Choose</button>
  </section>

  <section class="card card--create">
    <h2 class="card-title">Create</h2>
    <p class="card-lede">Big changes for the biggest savings Generate your own power and kill your bill.</p>
    <ul class="card-list">
      <li>Solar</li>
      <li>EV Chargers</li>
      <li>Energy Storage</li>
    </ul>
    <button class="choose-btn">Choose</button>
  </section>
</body>
</html>
```